Elegant Business Card for Technology Company

Client is a supplier of innovative industrial communications and automation equipment since 2002. This contest is to gather fresh ideas for a redesign of the existing business card. Client is looking for design that best communicates tagline "Industrial Networking and Computing Specialist".

Design submissions should look modern, clean, elegant and professional. It should not be cluttered. Use white as the primary colour. Orange and black as secondary colour. Refer to jpeg File 1 on the current design.

Fonts used by Client used include Arial Regular, Arial Black, Roboto Regular, Roboto Black and Lato.

The winning design will be sent for offset printing using super white 250gsm artcard paper (open for suggestions).

Target Market(s)

System Engineers, Project Managers, Purchasing Managers from companies providing engineering services for Smart Cities.

Industry/Entity Type

Information Technology

Contact Information for Business Card

Refer to PDF File 3 for Business Card Details. Priority of short contact information would be as follows Name > Job Title > Email > Mobile > Web > Tel > Fax > Business Address >UEN (UEN represents company registration number)

Font styles to use
Sans Serif

Colors
ffffff
f37122
000000
5c5c5c

Requirements
Must have
• Refer to AI File 2 (Company Logo) & PDF File 3 (Information on Namecard)
Should not have
• No QR codes
• No Social Media Icons
• Do not create full Black or Orange colour background

```html
<!DOCTYPE html>
<html lang="en">
<head>
<meta charset="utf-8">
<title>Korvane Business Card</title>
<link rel="stylesheet" href="https://fonts.googleapis.com/css2?family=Lato:wght@400;700;900&display=swap">
<style>
  :root {
    --white: #ffffff;
    --orange: #f37122;
    --black: #000000;
    --grey: #5c5c5c;
    --stage: #2b2b2b;
  }
  * { box-sizing: border-box; margin: 0; padding: 0; }
  html, body { width: 1200px; height: 1189px; overflow: hidden; }
  body {
    background: var(--stage);
    font-family: "Lato", Arial, sans-serif;
    color: var(--black);
    position: relative;
  }
  .card {
    position: absolute;
    left: 150px;
    width: 900px;
    height: 514px;
    background: var(--white);
    border-radius: 26px;
    overflow: hidden;
  }
  .card--front { top: 36px; }
  .card--back { top: 620px; }
  .card__band {
    position: absolute;
    left: 0; right: 0; bottom: 0;
    height: 26px;
    background: var(--black);
  }

  /* Wordmark */
  .wordmark {
    display: flex;
    align-items: center;
    gap: 12px;
    white-space: nowrap;
  }
  .wordmark__dot {
    border-radius: 50%;
    background: var(--orange);
    flex: none;
  }
  .wordmark__name {
    font-weight: 900;
    letter-spacing: 1px;
    color: var(--black);
  }
  .wordmark--front .wordmark__dot { width: 46px; height: 46px; }
  .wordmark--front .wordmark__name { font-size: 46px; }
  .wordmark--back .wordmark__dot { width: 54px; height: 54px; }
  .wordmark--back .wordmark__name { font-size: 54px; }

  /* Front */
  .front__web {
    position: absolute;
    top: 46px; right: 60px;
    font-size: 17px;
    color: var(--orange);
  }
  .front__brand {
    position: absolute;
    top: 112px; left: 50px;
    display: flex;
    align-items: flex-end;
    gap: 16px;
    white-space: nowrap;
  }
  .front__company {
    font-size: 24px;
    font-weight: 400;
    padding-bottom: 6px;
  }
  .front__person {
    position: absolute;
    top: 196px; right: 70px;
    white-space: nowrap;
  }
  .front__name { font-size: 30px; font-weight: 700; line-height: 34px; }
  .front__title { font-size: 19px; color: var(--orange); margin-left: 54px; line-height: 22px; }
  .front__rule {
    position: absolute;
    top: 270px; left: 40px; right: 120px;
    height: 1.5px;
    background: var(--orange);
  }
  .contacts {
    position: absolute;
    top: 296px; left: 50px;
    list-style: none;
  }
  .contacts li {
    display: flex;
    align-items: center;
    gap: 10px;
    font-size: 22px;
    line-height: 34px;
    white-space: nowrap;
  }
  .contacts svg {
    width: 22px; height: 22px;
    background: var(--orange);
    border-radius: 3px;
    padding: 3px;
    flex: none;
  }
  .front__address {
    position: absolute;
    top: 300px; right: 66px;
    font-size: 21px;
    line-height: 30px;
    text-align: right;
    font-style: normal;
    white-space: nowrap;
  }

  /* Back */
  .back__brand {
    position: absolute;
    top: 62px; left: 0; right: 0;
    display: flex;
    justify-content: center;
  }
  .back__tagline {
    position: absolute;
    top: 168px; left: 0; right: 0;
    text-align: center;
    font-size: 30px;
    font-weight: 400;
  }
  .back__rule {
    position: absolute;
    top: 222px; left: 60px; right: 60px;
    border-top: 3px dotted var(--orange);
  }
  .services {
    position: absolute;
    top: 240px; left: 0; right: 0;
    list-style: none;
    text-align: center;
    font-size: 24px;
    line-height: 34px;
  }
  .back__uen {
    position: absolute;
    left: 0; right: 0; bottom: 0;
    height: 46px;
    background: var(--black);
    color: var(--white);
    text-align: center;
    font-size: 24px;
    line-height: 46px;
  }
  .back__uen-number { color: var(--orange); margin-left: 12px; font-size: 28px; }
</style>
</head>
<body>

<section class="card card--front" aria-label="Business card front">
  <p class="front__web">www.korvane.com</p>

  <div class="front__brand">
    <div class="wordmark wordmark--front">
      <span class="wordmark__dot"></span>
      <span class="wordmark__name">KORVANE</span>
    </div>
    <span class="front__company">Korvane Asia Pacific Pte Ltd</span>
  </div>

  <div class="front__person">
    <p class="front__name">Adrian Lim</p>
    <p class="front__title">Sales Manager</p>
  </div>

  <div class="front__rule"></div>

  <ul class="contacts">
    <li>
      <svg viewBox="0 0 16 16" aria-hidden="true"><rect x="4.5" y="1.5" width="7" height="13" rx="1.2" fill="none" stroke="#fff" stroke-width="1.4"/><circle cx="8" cy="12" r="0.9" fill="#fff"/></svg>
      +65 8123 4567
    </li>
    <li>
      <svg viewBox="0 0 16 16" aria-hidden="true"><path d="M2 6c0-2 2-3 6-3s6 1 6 3v1h-3V5.5H5V7H2z" fill="#fff"/><rect x="3" y="8" width="10" height="6" rx="1" fill="#fff"/></svg>
      +65 6555 0140
    </li>
    <li>
      <svg viewBox="0 0 16 16" aria-hidden="true"><rect x="4" y="2" width="8" height="5" fill="none" stroke="#fff" stroke-width="1.3"/><rect x="2" y="7" width="12" height="6" rx="1" fill="#fff"/></svg>
      +65 6555 0183
    </li>
    <li>
      <svg viewBox="0 0 16 16" aria-hidden="true"><rect x="2" y="4" width="12" height="8" fill="none" stroke="#fff" stroke-width="1.3"/><path d="M2 4l6 5 6-5" fill="none" stroke="#fff" stroke-width="1.3"/></svg>
      sales@korvane.com.sg
    </li>
  </ul>

  <address class="front__address">
    25 Kallang Way Lumen Park<br>
    #04-12 (Lobby B), Singapore 349311
  </address>

  <div class="card__band"></div>
</section>

<section class="card card--back" aria-label="Business card back">
  <div class="back__brand">
    <div class="wordmark wordmark--back">
      <span class="wordmark__dot"></span>
      <span class="wordmark__name">KORVANE</span>
    </div>
  </div>

  <h1 class="back__tagline">Industrial Networking and Computing Speciallist</h1>
  <div class="back__rule"></div>

  <ul class="services">
    <li>Industrial Ethernet / Wireless / Cellular</li>
    <li>Industrial and Emedded Computing</li>
    <li>Serial / Fieldbus Connectivity</li>
    <li>IP Video Surveillance</li>
    <li>Remote Automation</li>
  </ul>

  <p class="back__uen">UEN No<span class="back__uen-number">200299417</span></p>
</section>

</body>
</html>
```